I would like alternative creative proposals for our website header at tumbleoakhome.com.au
The current is seen as a bit too drab and dark. We would like to liven it up a bit. The logo will remain although we are open to alternative representation or styling. All submitted designs should include a version that has the existing logo (we do use it within a black circle in other marketing).
The fundamental features of the header must be present including brand logo, search, cart etc.
We want to expand our concept of how the header could appear and function and how it represents our business. Other web site expects will be redesigned to align.
Please become familiar with our business and what we are trying to achieve before submitting a design. We are about health, organic products, chemical free low toxin living, environmental sustainability, all delivered in a modern socially friendly way accessible to all demographics and walks of life with our primary focus on Australia. Our primary target demographic is Australian women between 35 and 55. If you would like more info then please send us some questions.
Development and full design is outside the scoop of this proposal. We are looking for "mockup" proposals for the new website header initially.

```html
<!DOCTYPE html>
<html lang="en">
<head>
<meta charset="utf-8">
<title>Tumble Oak Home – Header</title>
<link rel="stylesheet" href="https://fonts.googleapis.com/css2?family=Open+Sans:wght@400&display=swap">
<style>
  :root {
    --utility-green: #10a98f;
    --nav-grey: #a2a7ab;
    --masthead-bg: #f2f2f2;
    --ink: #111111;
    --accent-coral: #e8615a;
    --brand-teal: #10a98f;
  }
  * { box-sizing: border-box; margin: 0; padding: 0; }
  html, body {
    width: 1200px;
    height: 180px;
    overflow: hidden;
    background: var(--masthead-bg);
    font-family: "Open Sans", sans-serif;
    color: var(--ink);
  }
  .site-header { width: 1200px; height: 180px; display: flex; flex-direction: column; }

  .utility-bar {
    height: 44px;
    background: var(--utility-green);
    display: flex;
    justify-content: flex-end;
    align-items: center;
    gap: 22px;
    padding-right: 32px;
    font-size: 19px;
  }
  .utility-link { display: flex; align-items: center; gap: 2px; color: var(--ink); text-decoration: none; }
  .utility-link svg { display: block; }

  .account-nav {
    height: 44px;
    background: var(--nav-grey);
    display: flex;
    justify-content: flex-end;
    align-items: center;
    gap: 35px;
    padding-right: 32px;
  }
  .account-nav a { color: var(--ink); text-decoration: none; font-size: 19px; text-transform: uppercase; }

  .masthead {
    flex: 1;
    display: flex;
    align-items: center;
    justify-content: space-between;
    padding: 0 32px 0 20px;
  }
  .brand { display: flex; align-items: center; gap: 16px; text-decoration: none; color: var(--ink); }
  .brand-dot { width: 56px; height: 56px; border-radius: 50%; background: var(--brand-teal); }
  .brand-name { font-size: 45px; font-weight: 400; letter-spacing: 0.5px; line-height: 1; }

  .product-search {
    width: 290px;
    height: 54px;
    margin-top: 12px;
    display: flex;
    align-items: center;
    justify-content: space-between;
    border-bottom: 6px solid var(--ink);
  }
  .product-search input {
    border: none;
    background: transparent;
    font: inherit;
    font-size: 19px;
    color: var(--ink);
    width: 230px;
    outline: none;
  }
  .product-search input::placeholder { color: var(--ink); opacity: 1; }
  .search-button { border: none; background: transparent; padding: 0; margin-bottom: 10px; cursor: pointer; }
</style>
</head>
<body>
<header class="site-header">
  <div class="utility-bar">
    <a class="utility-link" href="#">
      <svg width="26" height="26" viewBox="0 0 26 26" aria-hidden="true">
        <g stroke="var(--accent-coral)" stroke-width="3" fill="var(--accent-coral)">
          <line x1="2" y1="24" x2="10" y2="16"/>
          <polygon points="13,13 6,14 12,20" stroke="none"/>
          <line x1="24" y1="2" x2="16" y2="10"/>
          <polygon points="13,13 20,12 14,6" stroke="none"/>
        </g>
      </svg>
      <span>Compare</span>
    </a>
    <a class="utility-link" href="#">
      <svg width="24" height="24" viewBox="0 0 24 24" aria-hidden="true">
        <path d="M12 22 C5 16 1 12 1 7.5 C1 4 3.6 1.5 6.6 1.5 C9 1.5 11 3 12 5 C13 3 15 1.5 17.4 1.5 C20.4 1.5 23 4 23 7.5 C23 12 19 16 12 22 Z" fill="var(--accent-coral)"/>
      </svg>
      <span>(0)</span>
    </a>
    <a class="utility-link" href="#">My Cart (0)</a>
  </div>

  <nav class="account-nav">
    <a href="#">My Account</a>
    <a href="#">Blog</a>
    <a href="#">Log In</a>
    <a href="#">Join</a>
  </nav>

  <div class="masthead">
    <a class="brand" href="#">
      <span class="brand-dot" aria-hidden="true"></span>
      <span class="brand-name">tumble oak home</span>
    </a>
    <form class="product-search" role="search">
      <input type="search" placeholder="Search for a product..." aria-label="Search for a product">
      <button class="search-button" type="submit" aria-label="Search">
        <svg width="32" height="26" viewBox="0 0 32 26" aria-hidden="true">
          <circle cx="10" cy="9" r="7" fill="none" stroke="var(--ink)" stroke-width="3"/>
          <line x1="15" y1="14" x2="29" y2="23" stroke="var(--ink)" stroke-width="5" stroke-linecap="round"/>
        </svg>
      </button>
    </form>
  </div>
</header>
</body>
</html>
```